Package design for small honey and vegetable farm

I would like to have a unique design for the packaging of our honey and vegetables. I have attached the logo from our farm "Willow Creek Acres" that should be on the packaging for both the honey and the vegetables

For the honey the writing, "100% pure organic honey" must be on the packaging in some place. As well as "from the busy bees at Willow Creek Acres". I have attached some designs that I like.

For the vegetables. The design will need to go on a box like the one in the attached image. The phrase "Organically Grown" should be on the package. I would like the background color of the package to be black. I think I would also like to see some stylized vegetables (tomatoes in particular) on the package.

I would like to be able to get all the colors (RGB) used in the designs so I can pass them on to printers.

Industry/Entity Type

Farm

Colors
fbee3e

Requirements
Must have
• For the honey, the package it must say "100% pure organic honey".
• For the vegetables I would like the background color to be black. I would also like some stylized vegetables (tomatoes in particular) added to the package.

```html
<!DOCTYPE html>
<html lang="en">
<head>
<meta charset="utf-8">
<title>Willow Creek Acres – Honey Label and Produce Box</title>
<link rel="stylesheet" href="https://fonts.googleapis.com/css2?family=Montserrat:wght@600&family=Comfortaa:wght@400&display=swap">
<style>
  :root {
    --page: #f4f4f2;
    --label-black: #1b1b1b;
    --comb-grey: #2b2b2b;
    --brand-yellow: #fbee3e;
    --honey-orange: #f0a81e;
    --honey-deep: #e38a0c;
    --leaf-green: #8cc63f;
    --pepper-red: #d8281e;
    --pepper-yellow: #f5b70f;
  }
  * { margin: 0; padding: 0; box-sizing: border-box; }
  html, body { width: 873px; height: 1200px; overflow: hidden; background: var(--page); }
  .canvas { position: relative; width: 873px; height: 1200px; }

  .honey-label { position: absolute; left: 236px; top: 40px; width: 400px; height: 420px; }
  .brand-name { font-family: "Montserrat", sans-serif; font-weight: 600; fill: var(--brand-yellow); }
  .arc-claim { font-family: "Comfortaa", sans-serif; font-size: 25px; fill: var(--honey-orange); }
  .origin-line { font-family: "Comfortaa", sans-serif; font-size: 14px; fill: var(--brand-yellow); }

  .box-panel {
    position: absolute; background: var(--label-black); height: 260px;
  }
  .box-panel--long { left: 36px; top: 500px; width: 800px; }
  .box-panel--short { left: 226px; top: 800px; width: 420px; }

  .panel-brand {
    position: absolute; font-family: "Montserrat", sans-serif; font-weight: 600;
    color: var(--brand-yellow); font-size: 34px; line-height: 1.15;
  }
  .panel-tagline {
    position: absolute; font-family: "Comfortaa", sans-serif; font-size: 24px;
    color: var(--leaf-green);
  }
  .box-panel--long .panel-brand { left: 44px; top: 80px; }
  .box-panel--long .panel-tagline { left: 44px; top: 168px; }
  .box-panel--short .panel-brand { left: 44px; top: 70px; }
  .box-panel--short .panel-tagline { left: 44px; top: 160px; }

  .produce-art {
    position: absolute; left: 400px; top: 50px; width: 370px; height: 160px; border-radius: 80px;
    background: linear-gradient(90deg, var(--pepper-red) 0%, var(--pepper-yellow) 38%, var(--pepper-red) 62%, #c91f17 100%);
  }
</style>
</head>
<body>
<main class="canvas">

  <svg class="honey-label" viewBox="0 0 400 420" aria-label="Honey jar label">
    <defs>
      <clipPath id="hex-clip">
        <polygon points="200,0 400,105 400,315 200,420 0,315 0,105"/>
      </clipPath>
      <linearGradient id="drop-gold" x1="0" y1="0" x2="0" y2="1">
        <stop offset="0" stop-color="#fbd23a"/>
        <stop offset="1" stop-color="#e89a10"/>
      </linearGradient>
      <path id="claim-arc" d="M133,297 A95,95 0 1 1 267,297"/>
    </defs>
    <polygon class="hex-base" points="200,0 400,105 400,315 200,420 0,315 0,105" fill="var(--label-black)"/>
    <g clip-path="url(#hex-clip)">
      <path class="comb-band" role="img" aria-label="Honeycomb pattern" d="M0,235 Q200,170 400,235 L400,420 L0,420 Z" fill="var(--comb-grey)"/>
    </g>
    <text class="brand-name" x="200" y="112" font-size="27" text-anchor="middle">Willow Creek Acres</text>
    <text class="arc-claim"><textPath href="#claim-arc" startOffset="50%" text-anchor="middle">100% pure organic honey</textPath></text>
    <path class="honey-drop" role="img" aria-label="Honey drop" d="M200,185 C190,205 168,228 168,252 A32,32 0 0 0 232,252 C232,228 210,205 200,185 Z" fill="url(#drop-gold)"/>
    <text class="origin-line" x="200" y="352" text-anchor="middle">from the busy bees</text>
    <text class="origin-line" x="200" y="372" text-anchor="middle">at Willow Creek Acres</text>
  </svg>

  <section class="box-panel box-panel--long" aria-label="Produce box, long side">
    <p class="panel-brand">Willow Creek Acres</p>
    <p class="panel-tagline">Organically Grown</p>
    <div class="produce-art" role="img" aria-label="Red and yellow bell peppers with two tomatoes"></div>
  </section>

  <section class="box-panel box-panel--short" aria-label="Produce box, short side">
    <p class="panel-brand">Willow Creek<br>Acres</p>
    <p class="panel-tagline">Organically Grown</p>
  </section>

</main>
</body>
</html>
```